Velmarone Website Redesign

We need a redesign of the company website.

We're a company, based in the UK, called Velmarone. We develop software for the Healthcare Industry, used by medical professionals throughout the UK on a daily basis.

We have a suite of tools that form the Velmarone Platform, and all are web-based.

We want to communicate that our software is not only innovative but is the best available, easy to use, and provides exceptional quality and RoI.

Additionally, we want our existing customers to be able to see what else we can offer them.

A site map is attached.
Updates

Hi Everyone,

As we approach the deadline for submissions, we’ve shortlisted threedesigns that we felt were the best of the submissions and have asked thedesigners to make some additional changes and produce some content pages so wecan see what’s beneath the Home page in the rest of the site.

Thank you all for your submissions – there was an awful lot ofdisagreement among everyone here over which designs we thought were best andsome of those that haven’t made it into the final three were very well liked.

Those in the final three have been messaged individually and have theirdesigns as the only non-eliminated ones showing. We would ask at this stagethat anyone not in the final three please do no further work or submitadditional designs as we are approaching the deadline and will not be able toprovide sufficient feedback to allow any changes in a short space of time.

Kind regards,
The Velmarone Team

Target Market(s)

Nurses and medical professionals in western-speaking countries, most notably in the UK.

Predominantly, we expect it will be senior medical staff that will be viewing (and using) our website - some will be existing customers and some will be new or potential customers.

Industry/Entity Type

Medical

Requirements
Must have
• Area to showcase and provide information about products.
• Company information - who we are and why you should choose us.
• News and events - blog, archive newsletters, publications, etc.
• Support section for existing customers - FAQ, Forum, Manuals.
• Contact page.
• We also feel that we'd like to have our telephone number and primary email address visible at all times, with an immediate ability for users to request a demonstration.
Nice to have
• A "My Velmarone" area would be nice at some point, though that's something for further down the line.

```html
<!DOCTYPE html>
<html lang="en">
<head>
<meta charset="utf-8">
<title>Velmarone – Bringing Technology to Healthcare</title>
<link rel="stylesheet" href="https://fonts.googleapis.com/css2?family=Arimo:wght@400;700&family=PT+Sans:wght@400;700&family=Open+Sans:wght@400;600;700&display=swap">
<style>
:root{
  --backdrop:#0d3c44;
  --frame:#ffffff;
  --page-top:#cfe0f7;
  --page-bottom:#eef5fd;
  --brand-blue:#1a8ee6;
  --deep-blue:#1c6fb5;
  --link-blue:#0a4fd0;
  --text:#333b44;
  --muted:#6d7378;
  --grey-logo:#8a8f94;
  --orange:#f26a10;
  --green:#34a043;
  --sub-green:#d8f3d2;
  --cyan:#19b4d8;
  --nav-top:#e9e9e9;
  --nav-bottom:#b9b9b9;
  --footer-top:#8a8a8a;
  --footer-bottom:#4e4e4e;
}
*{box-sizing:border-box;margin:0;padding:0}
html,body{width:933px;height:1200px;overflow:hidden}
body{background:var(--backdrop);font-family:"Open Sans",Arial,sans-serif;color:var(--text);position:relative}
.abs{position:absolute}
.frame{left:62px;top:54px;width:812px;height:1090px;background:var(--frame);border-radius:4px}
.page{left:66px;top:58px;width:804px;height:1082px;background:linear-gradient(var(--page-top),#f4f8fe 120px,var(--page-bottom) 380px,#e4eefb 760px,#f1f6fd);overflow:hidden}

.wordmark{left:108px;top:84px;font-family:Arimo,Arial,sans-serif;font-weight:700;font-size:38px;color:var(--brand-blue);letter-spacing:-.5px}
.tagline{left:109px;top:136px;font-family:Arimo,Arial,sans-serif;font-weight:700;font-size:16px;color:var(--grey-logo)}
.session{left:636px;top:111px;font-size:11.5px;color:#333}
.session b{color:var(--orange);font-weight:400}
.search{left:678px;top:142px;width:142px;height:15px;background:#fff;border:1px solid #d5dbe3;border-radius:3px;font-size:10.5px;color:#bbb;padding-left:4px;line-height:13px}
.search-icon{left:652px;top:139px}

.nav{left:66px;top:180px;width:804px;height:32px;background:linear-gradient(var(--nav-top),var(--nav-bottom));display:flex;box-shadow:0 2px 3px rgba(0,0,0,.2)}
.nav a{flex:auto;text-align:center;font-size:12.5px;color:#444;text-decoration:none;line-height:32px;border-right:1px solid #a7a7a7}
.nav a:last-child{border:0}
.nav a.current{background:linear-gradient(#fafafa,#dcdcdc);color:var(--brand-blue)}
.subnav{left:66px;top:215px;width:804px;height:17px;background:var(--sub-green);display:flex;justify-content:space-around;align-items:center;font-size:9px;color:#666}
.subnav span.current{color:var(--brand-blue)}
.subnav i{width:4px;height:4px;background:#9cc6e8;display:block}

.hero-strip{left:70px;top:236px;width:36px;height:190px;background:#73c9ea}
.hero-photo{left:106px;top:236px;width:292px;height:190px;background:linear-gradient(120deg,#e9f1f7,#c9d7e4 60%,#f2f4f6)}
.hero-panel{left:398px;top:236px;width:470px;height:190px;background:linear-gradient(90deg,#cde9f4,#eef6fb)}
.hero-title{left:435px;top:270px;font-family:"PT Sans",sans-serif;font-size:26px;color:#111;line-height:1.3}
.hero-title span{display:block;font-size:30px;color:var(--brand-blue)}
.hero-title strong{font-weight:700}
.hero-copy{left:436px;top:343px;width:390px;font-size:10.5px;line-height:15px;color:#333}
.more-info{left:756px;top:390px;width:74px;height:21px;background:linear-gradient(#4a9bff,#0a4fd8);border-radius:3px;color:#fff;font-size:11px;text-align:center;line-height:21px}

.section-tag{height:25px;width:182px;color:#fff;font-family:"PT Sans",sans-serif;font-size:20px;padding-left:10px;line-height:25px}
.about-tag{left:98px;top:455px;background:var(--deep-blue)}
.news-tag{left:98px;top:650px;background:var(--green)}
.body-copy{font-size:9px;line-height:12px;text-align:justify;color:#333}
.body-copy p{text-indent:22px;margin-bottom:12px}
.about-copy{left:108px;top:486px;width:218px}
.read-more{font-size:10px}
.about-more{left:248px;top:618px;color:var(--cyan)}
.about-photo{left:338px;top:484px;width:238px;height:137px;background:linear-gradient(100deg,#c9d3dc,#e8edf0 50%,#9fb2c3)}
.news-photo{left:97px;top:684px;width:182px;height:119px;background:linear-gradient(110deg,#dfe7ee,#f4f6f8 50%,#c5d1dc)}
.news-list{left:300px;top:682px;width:280px;list-style:none;font-size:9.8px;line-height:12px}
.news-list li{position:relative;padding-left:17px;margin-bottom:13px}
.news-list li::before{content:"";position:absolute;left:0;top:4px;width:7px;height:7px;background:currentColor}
.news-list a{text-decoration:underline;color:inherit}
.n-blue{color:var(--link-blue)}.n-orange{color:var(--orange)}.n-green{color:var(--green)}

.blog-title{left:104px;top:847px;font-family:"PT Sans",sans-serif;font-size:20px;color:var(--orange)}
.blog-copy{left:104px;top:878px;width:285px}
.rss{left:430px;top:887px}
.blog-bar{left:98px;top:1009px;width:488px;height:18px;background:#dff3f6}
.blog-more{left:496px;top:1011px;color:var(--orange)}

.login{left:614px;top:445px;width:233px;height:210px;border:2px solid #fff;border-radius:12px;background:linear-gradient(#b5dcf8,#63c2f4 70%,#8fd3f7);box-shadow:0 0 6px rgba(0,0,0,.15)}
.login-title{left:644px;top:455px;font-family:"PT Sans",sans-serif;font-size:25px;color:var(--link-blue)}
.login-rule{left:638px;top:490px;width:185px;height:1px;background:rgba(255,255,255,.7)}
.field-label{font-size:9px;color:#333}
.field{width:196px;height:18px;background:#d9e3ea;border:1px solid #c6d1da;border-radius:3px;font-size:10px;color:#9aa;padding-left:6px;line-height:16px}
.checkbox{left:637px;top:581px;width:11px;height:11px;background:#fff;border:1px solid #999}
.remember{left:654px;top:582px;font-size:8.5px;color:#333}
.remember b{color:var(--orange);font-weight:400}
.btn-grey{background:linear-gradient(#fff,#bdbdbd);border:1px solid #999;border-radius:5px;color:#222;text-align:center}
.login-btn{left:762px;top:588px;width:68px;height:20px;font-size:11px;line-height:18px}
.login-links{left:639px;top:616px;font-size:8px;line-height:12px;color:#1c3f8c;text-decoration:underline}

.demo{left:615px;top:670px;width:231px;height:38px;border-radius:3px;background:linear-gradient(#38a8ff,#0a36d8);border:1px solid #e8c87a;color:#fff;font-family:"PT Sans",sans-serif;font-weight:700;font-size:16px;text-align:center;line-height:36px;letter-spacing:.5px}
.newsletter{left:615px;top:722px;width:231px;height:68px;border-radius:3px;background:linear-gradient(#e8f8df,#5cc04a);border:1px solid #8fcf7e}
.newsletter-title{left:632px;top:730px;font-family:"PT Sans",sans-serif;font-size:18px;color:#333}
.nl-field{left:634px;top:760px;width:130px;height:18px;background:#eef2ee;border-radius:9px 0 0 9px;font-size:8px;color:#999;padding-left:12px;line-height:18px}
.nl-btn{left:762px;top:759px;width:68px;height:20px;font-size:10.5px;line-height:18px}

.archive{left:615px;top:807px;width:232px;height:210px;border:2px solid #fff;border-radius:12px;background:linear-gradient(#fbfdfd,#e2f3d2 40%,#8bd26a);box-shadow:0 0 6px rgba(0,0,0,.15)}
.archive-title{left:641px;top:818px;font-family:"PT Sans",sans-serif;font-size:17.5px;color:#222}
.archive-list{left:657px;top:850px;list-style:none;font-size:12px;line-height:18px}
.archive-list li{text-decoration:underline;color:#222}

.footer{left:70px;top:1036px;width:796px;height:100px;background:linear-gradient(var(--footer-top),var(--footer-bottom))}
.footer-contact{left:87px;top:1049px;font-size:11px;line-height:15px;color:#fff}
.footer-contact h4{font-size:11px;font-weight:700;letter-spacing:.3px}
.footer-lines{left:440px;top:1056px;font-family:"PT Sans",sans-serif;font-size:27px;line-height:30px;color:#fff;text-shadow:1px 1px 2px rgba(0,0,0,.4)}
.footer-lines b{color:#f5a623;font-weight:400}
</style>
</head>
<body>
<div class="abs frame"></div>
<div class="abs page"></div>

<header>
  <div class="abs wordmark">VelmaroneHealth</div>
  <div class="abs tagline">Bringing Technology to Healthcare</div>
  <div class="abs session">You are logged in as <b>Daniel Hartley</b></div>
  <svg class="abs search-icon" width="26" height="26" viewBox="0 0 26 26" aria-hidden="true">
    <circle cx="10" cy="10" r="7" fill="#dff0fb" stroke="#3a6f9e" stroke-width="2.5"/>
    <line x1="15" y1="15" x2="23" y2="23" stroke="#3a6f9e" stroke-width="4" stroke-linecap="round"/>
  </svg>
  <div class="abs search">Search Velmarone</div>
</header>

<nav class="abs nav">
  <a>Home</a><a>Products &amp; Services</a><a class="current">About Velmarone</a><a>News and Events</a><a>Support</a><a>Contact us</a><a>My Velmarone</a>
</nav>
<div class="abs subnav">
  <span class="current">About Velmarone</span><i></i><span>Leadership Team</span><i></i><span>Advisory Board</span><i></i><span>Partnerships</span><i></i><span>Experienced Clinical Staff</span><i></i><span>Medical Solutions Architects</span><i></i><span>Clients List</span>
</div>

<section>
  <div class="abs hero-strip"></div>
  <div class="abs hero-photo" role="img" aria-label="Photo of three doctors in white coats smiling around a laptop"></div>
  <div class="abs hero-panel"></div>
  <svg class="abs" style="left:410px;top:255px" width="16" height="16" aria-hidden="true"><path d="M0 0H16V16L10 6Z" fill="#fff"/></svg>
  <h1 class="abs hero-title" style="font-weight:400">WE DEVELOPE SOFTWARES FOR THE<span><strong>HEALTHCARE</strong> INDUSTRY</span></h1>
  <p class="abs hero-copy">We develop software for the Healthcare Industry, used by medical professionals throughout the UK on a daily basis. We have a suite of tools that form the Velmarone Platform, and all are web-based.</p>
  <div class="abs more-info">More Info</div>
</section>

<main>
  <h2 class="abs section-tag about-tag" style="font-weight:400">About Velmarone</h2>
  <div class="abs body-copy about-copy">
    <p>In today's changing environment, healthcare organisations globally are faced with conflicting challenges; to reduce costs while offering improved healthcare services to patients that expect better and better services.</p>
    <p>Most health care organisations operate using either [rent technologies and systems that have been developed over a long period of time, ..........</p>
  </div>
  <div class="abs read-more about-more">...... read more</div>
  <div class="abs about-photo" role="img" aria-label="Photo of a doctor seated beside a monitor showing a medical scan"></div>

  <h2 class="abs section-tag news-tag" style="font-weight:400">News and Events</h2>
  <div class="abs news-photo" role="img" aria-label="Photo of two doctors working together at a laptop"></div>
  <ul class="abs news-list">
    <li class="n-blue"><a>Our New product launch in UK region. This weeks top Story. for more information click here .....</a></li>
    <li class="n-orange"><a>Dr. Elspeth Moran has invented new range of products&nbsp; for more information click here .....</a></li>
    <li class="n-green"><a>This years revolution in medical industry.</a></li>
  </ul>

  <h2 class="abs blog-title" style="font-weight:400">VELMARONE NEWS BLOG</h2>
  <div class="abs body-copy blog-copy">
    <p>In today's changing environment, healthcare organisations globally are faced with conflicting challenges; to reduce costs while offering improved healthcare services to patients that expect better and better services.</p>
    <p>Most health care organisations operate using either manual paper based processed or a mix of different technologies and systems that have been developed over avices to patients that expect better and better services.</p>
  </div>
  <svg class="abs rss" width="102" height="100" viewBox="0 0 102 100" aria-label="Feed icon" role="img">
    <defs><linearGradient id="feedFill" x1="0" y1="0" x2="0" y2="1"><stop offset="0" stop-color="#ff8a1a"/><stop offset="1" stop-color="#e2500a"/></linearGradient></defs>
    <rect x="2" y="2" width="98" height="90" rx="14" fill="url(#feedFill)"/>
    <circle cx="26" cy="68" r="9" fill="#fff"/>
    <path d="M18 42a32 32 0 0 1 34 34" fill="none" stroke="#fff" stroke-width="10" stroke-linecap="round"/>
    <path d="M18 20a54 54 0 0 1 56 56" fill="none" stroke="#fff" stroke-width="10" stroke-linecap="round"/>
  </svg>
  <div class="abs blog-bar"></div>
  <div class="abs read-more blog-more">...... read more</div>
</main>

<aside>
  <div class="abs login"></div>
  <div class="abs login-title">Login</div>
  <div class="abs login-rule"></div>
  <div class="abs field-label" style="left:635px;top:513px">E-mail ID / Login ID</div>
  <div class="abs field" style="left:634px;top:524px"></div>
  <div class="abs field-label" style="left:635px;top:545px">Password</div>
  <div class="abs field" style="left:634px;top:558px">&bull;&bull;&bull;&bull;&bull;&bull;&bull;&bull;&bull;&bull;&bull;&bull;&bull;&bull;&bull;&bull;</div>
  <div class="abs checkbox"></div>
  <div class="abs remember">Remember <b>Me</b></div>
  <div class="abs btn-grey login-btn">Login</div>
  <div class="abs login-links">Forgot your passward?<br>Sign up here</div>

  <div class="abs demo">REQUEST A DEMO</div>

  <div class="abs newsletter"></div>
  <div class="abs newsletter-title">Subscribe for Newsletter</div>
  <div class="abs nl-field">Enter your e-mail ID here</div>
  <div class="abs btn-grey nl-btn">Subscribe</div>

  <div class="abs archive"></div>
  <div class="abs archive-title">Archieved Newsletters</div>
  <ul class="abs archive-list">
    <li>January 2009</li><li>March 2009</li><li>June 2009</li><li>September 2009</li><li>December 2009</li><li>January 2010</li><li>March 2010</li>
  </ul>
</aside>

<footer>
  <div class="abs footer"></div>
  <div class="abs footer-contact">
    <h4>CONTACT INFORMATION</h4>
    Velmarone - # 48 Kestrel Lane, London N7 2QD,<br>United Kingdom<br>
    Tel.: +44 (0) 207 555 0142&nbsp; +44 (0) 207 555 0142<br>
    <b>Fax:</b> +44 (0) 207 555 0198
  </div>
  <div class="abs footer-lines">
    <div>&nbsp;&nbsp;<b>Call :</b> +44 (0) 207 555 0142</div>
    <div><b>E-Mail :</b> support@velmarone.com</div>
  </div>
</footer>
</body>
</html>
```